New Cleaning Business, require full Plumtalk set up, content, images, layout.

we need a social presence and want a fresh, vibrant look that speaks for its self. we specialise in end of lease cleaning, vindle cleaning and management and residential cleaning. we also offer property management, set up, furniture styling and photography

uploaded logo and a couple of property pics to give an idea. Open to designers suggestions

I have already created a Plumtalk page with company name
please contact me via email with any questions

Real estate Company, Owners, tenants and vindle host

Cleaning Service

• professional clean look

```html
<!DOCTYPE html>
<html lang="en">
<head>
<meta charset="utf-8">
<title>Pure Nest – Cover</title>
<link href="https://fonts.googleapis.com/css2?family=Montserrat:wght@300;400;600;700&display=swap" rel="stylesheet">
<style>
  :root {
    --navy: #24457a;
    --green: #7cae47;
    --ink: #555a60;
    --paper: #ffffff;
    --backdrop: #eef0f2;
    --panel-light: #f4f4f4;
  }
  html, body {
    margin: 0;
    padding: 0;
    width: 874px;
    height: 1200px;
    overflow: hidden;
    background: var(--backdrop);
    font-family: "Montserrat", sans-serif;
  }
  .canvas {
    position: relative;
    width: 874px;
    height: 1200px;
  }
  .cover {
    position: absolute;
    left: 20px;
    top: 382px;
    width: 900px;
    height: 470px;
    transform: scale(0.9267);
    transform-origin: top left;
    background: linear-gradient(100deg, var(--panel-light) 0%, var(--paper) 45%);
    box-shadow: 0 6px 18px rgba(0,0,0,0.18);
    overflow: hidden;
  }
  .brand {
    position: absolute;
    left: 70px;
    top: 52px;
    width: 260px;
    text-align: center;
  }
  .brand-name {
    display: inline-flex;
    align-items: center;
    gap: 10px;
    font-size: 30px;
    font-weight: 600;
    letter-spacing: 2px;
    color: var(--navy);
  }
  .brand-mark {
    width: 16px;
    height: 16px;
    border-radius: 50%;
    background: var(--green);
  }
  .brand-tagline {
    display: flex;
    align-items: center;
    justify-content: center;
    gap: 8px;
    margin-top: 6px;
    font-size: 13px;
    color: var(--ink);
  }
  .brand-tagline::before,
  .brand-tagline::after {
    content: "";
    width: 30px;
    height: 1px;
    background: var(--ink);
  }
  .offer {
    position: absolute;
    left: 82px;
    top: 167px;
    width: 238px;
    height: 210px;
    background: var(--green);
    color: var(--paper);
    box-sizing: border-box;
    padding: 28px 26px;
  }
  .offer-title {
    margin: 0;
    font-size: 26px;
    font-weight: 700;
    letter-spacing: 1px;
  }
  .offer-rule {
    width: 46px;
    height: 3px;
    background: var(--paper);
    margin: 4px 0 12px;
  }
  .offer-list {
    list-style: none;
    margin: 0;
    padding: 0;
    font-size: 16px;
    font-weight: 400;
    line-height: 26px;
  }
  .offer-list li::before {
    content: "";
    display: inline-block;
    width: 6px;
    height: 6px;
    border-radius: 50%;
    background: var(--paper);
    margin-right: 12px;
    vertical-align: middle;
  }
  .specialty {
    position: absolute;
    left: 20px;
    top: 393px;
    width: 380px;
    height: 51px;
    background: var(--navy);
    color: var(--paper);
    text-align: center;
    font-size: 11.5px;
    line-height: 14px;
    box-sizing: border-box;
    padding-top: 10px;
  }
  .specialty strong { font-weight: 700; }
  .photo {
    position: absolute;
  }
  .photo-bedroom-view { left: 425px; top: 17px; width: 461px; height: 216px;
    background: linear-gradient(90deg, #6f7e88 0%, #8c8f8e 35%, #8a6a52 60%, #c9b8a6 100%); }
  .photo-kitchen { left: 426px; top: 235px; width: 151px; height: 214px;
    background: linear-gradient(180deg, #c7ccd0 0%, #e6e6e4 60%, #9d8f80 100%); }
  .photo-cushions { left: 580px; top: 235px; width: 151px; height: 214px;
    background: linear-gradient(180deg, #e8e2dc 0%, #c7a9a4 40%, #e9e7e4 70%, #d9d7d3 100%); }
  .photo-bathroom { left: 734px; top: 235px; width: 152px; height: 214px;
    background: linear-gradient(90deg, #e6e6e6 0%, #d8d8d8 30%, #2f3540 35%, #4d5562 100%); }
</style>
</head>
<body>
<div class="canvas">
  <section class="cover">
    <div class="brand">
      <div class="brand-name"><span class="brand-mark"></span>PURE NEST</div>
      <div class="brand-tagline">Eco Friendly Services</div>
    </div>

    <div class="offer">
      <h2 class="offer-title">WE OFFER</h2>
      <div class="offer-rule"></div>
      <ul class="offer-list">
        <li>Property Management</li>
        <li>Set Up</li>
        <li>Furniture Styling</li>
        <li>Photography</li>
      </ul>
    </div>

    <div class="specialty">
      We Specialise in End Of Lease Cleaning,<br>
      <strong>vindle Cleaning</strong> and <strong>Management</strong> and <strong>Residential Cleaning</strong>
    </div>

    <div class="photo photo-bedroom-view" role="img" aria-label="Styled bedroom with city skyline view through floor-to-ceiling windows"></div>
    <div class="photo photo-kitchen" role="img" aria-label="Bright apartment kitchen beside a window with a pot plant"></div>
    <div class="photo photo-cushions" role="img" aria-label="Made bed with colourful cushions under abstract artwork"></div>
    <div class="photo photo-bathroom" role="img" aria-label="Modern bathroom with dark tiles and glass shower"></div>
  </section>
</div>
</body>
</html>
```